Business Card Design

Our Motto is "Protecting Australia's Underground Utilities"

We want the Southern Cross inside a shield I have attached the southern cross and our old shield design

Product description is: Vacuum Excavation & Utility Location
Wet & Dry Vacuum Loading
Confined Space Entry Specialists
High Pressure Cleaning

The Southern Cross in the shield must be blue and white. The Company name must be Coastal Pipeguard Services. The Green & Gold Shield logo I uploaded is my OLD logo design. Thank you

Target Market(s)

Civil Construction

Industry/Entity Type

Business

Contact Information for Business Card

Coastal Pipeguard Services Pty Ltd
Corey Halbrook(Director)
0413862975
coreyh@pipeguardco.com.au
A.B.N.52938470116

Colors
0456a3

Requirements
Must have
• Southern Cross inside a shield, Blue and white design on the Southern Cross shield.
Must say Coastal Pipeguard Services P/L

```html
<!DOCTYPE html>
<html lang="en">
<head>
<meta charset="utf-8">
<title>Coastal Pipeguard Services – Business Card</title>
<link rel="stylesheet" href="https://fonts.googleapis.com/css2?family=Archivo:wdth,wght@125,400;125,600;125,800&display=swap">
<style>
  :root {
    --ink-black: #000000;
    --paper-white: #ffffff;
    --brand-blue: #0a2fd6;
    --brand-deep: #0456a3;
    --sky-light: #9ff4fb;
    --sky-mid: #3fd6f2;
    --sky-deep: #0a8ff0;
    --ocean: #0b63e8;
    --text-white: #ffffff;
  }
  * { margin: 0; padding: 0; box-sizing: border-box; }
  html, body {
    width: 1200px;
    height: 742px;
    overflow: hidden;
    background: var(--paper-white);
  }
  .card {
    position: relative;
    width: 1200px;
    height: 742px;
    background: var(--paper-white);
    border: 4px solid var(--ink-black);
    font-family: "Archivo", "Arial", sans-serif;
    font-stretch: 125%;
  }
  .card-face {
    position: absolute;
    left: 18px;
    top: 18px;
    width: 1156px;
    height: 700px;
    border: 2px solid var(--ink-black);
    overflow: hidden;
  }
  .card-face svg.backdrop {
    position: absolute;
    inset: 0;
    width: 100%;
    height: 100%;
  }
  .brand-mark {
    position: absolute;
    left: 112px;
    top: 58px;
    width: 200px;
    height: 200px;
    border-radius: 50%;
    background: var(--brand-blue);
  }
  .company-name {
    position: absolute;
    left: 0;
    top: 322px;
    width: 416px;
    text-align: center;
    color: var(--brand-blue);
    font-weight: 400;
    font-size: 35px;
    line-height: 36px;
    letter-spacing: 1px;
    text-transform: uppercase;
  }
  .person-name {
    position: absolute;
    right: 12px;
    top: 28px;
    color: var(--brand-blue);
    font-weight: 800;
    font-size: 46px;
    letter-spacing: 2px;
    text-transform: uppercase;
    white-space: nowrap;
  }
  .person-role {
    position: absolute;
    right: 32px;
    top: 82px;
    color: var(--text-white);
    font-weight: 400;
    font-size: 25px;
    letter-spacing: 2px;
    text-transform: uppercase;
  }
  .contact-row {
    position: absolute;
    left: 553px;
    display: flex;
    align-items: center;
  }
  .contact-row.phone { top: 141px; }
  .contact-row.email { top: 211px; }
  .contact-icon {
    width: 54px;
    height: 54px;
    flex: none;
  }
  .contact-text {
    margin-left: 32px;
    white-space: nowrap;
  }
  .phone .contact-text {
    color: var(--brand-blue);
    font-size: 37px;
    letter-spacing: 3px;
  }
  .email .contact-text {
    color: var(--text-white);
    font-size: 25px;
    letter-spacing: 0.5px;
  }
  .motto {
    position: absolute;
    left: 0;
    width: 100%;
    top: 582px;
    text-align: center;
    color: var(--brand-blue);
    font-weight: 400;
    font-size: 38px;
    letter-spacing: 1px;
    white-space: nowrap;
  }
  .abn {
    position: absolute;
    left: 0;
    width: 100%;
    top: 664px;
    text-align: center;
    color: var(--text-white);
    opacity: 0.92;
    font-size: 27px;
    letter-spacing: 1px;
  }
</style>
</head>
<body>
<div class="card">
  <div class="card-face">
    <svg class="backdrop" viewBox="0 0 1156 700" preserveAspectRatio="none" aria-hidden="true">
      <defs>
        <linearGradient id="sky" x1="0" y1="0" x2="1" y2="0">
          <stop offset="0" stop-color="#1aa8f4"/>
          <stop offset="0.2" stop-color="#3fd0f4"/>
          <stop offset="0.45" stop-color="#a4f7fc"/>
          <stop offset="0.7" stop-color="#3fd6f2"/>
          <stop offset="0.88" stop-color="#0b8ef2"/>
          <stop offset="1" stop-color="#1aa8f4"/>
        </linearGradient>
        <linearGradient id="fade" x1="0" y1="0" x2="0" y2="1">
          <stop offset="0" stop-color="#ffffff" stop-opacity="0.0"/>
          <stop offset="1" stop-color="#ffffff" stop-opacity="0.25"/>
        </linearGradient>
      </defs>
      <rect width="1156" height="700" fill="url(#sky)"/>
      <path d="M0 80 C140 60 260 160 320 320 C380 480 460 640 520 700 L0 700 Z" fill="#0b63e8" opacity="0.35"/>
      <path d="M1156 0 L780 0 C900 60 980 180 1000 320 C1020 460 980 600 960 700 L1156 700 Z" fill="#0b63e8" opacity="0.45"/>
      <path d="M1156 40 C1050 120 1000 260 1020 420 C1040 560 1120 640 1156 680 Z" fill="#0a8ff0" opacity="0.5"/>
      <path d="M80 700 C120 520 160 360 110 160" stroke="#ffffff" stroke-opacity="0.35" stroke-width="14" fill="none"/>
      <path d="M970 700 C1010 520 1020 320 960 120" stroke="#ffffff" stroke-opacity="0.4" stroke-width="12" fill="none"/>
      <path d="M0 520 C300 470 700 540 1156 380 L1156 700 L0 700 Z" fill="url(#fade)"/>
    </svg>

    <div class="brand-mark" aria-hidden="true"></div>
    <div class="company-name">Coastal<br>Pipeguard<br>Services<br>P/L</div>

    <div class="person-name">Corey Halbrook</div>
    <div class="person-role">Director</div>

    <div class="contact-row phone">
      <svg class="contact-icon" viewBox="0 0 54 54" aria-hidden="true">
        <rect x="2" y="2" width="50" height="50" rx="8" fill="#0b8ef2"/>
        <rect x="6" y="6" width="42" height="40" rx="6" fill="#e8fbff"/>
        <path d="M18 14 l5 -1 l3 8 l-3 3 c2 4 5 7 9 9 l3 -3 l8 3 l-1 5 c-1 2 -3 3 -5 3 c-11 -1 -21 -11 -22 -22 c0 -2 1 -4 3 -5 z" fill="none" stroke="#0a2fd6" stroke-width="2.4" stroke-linejoin="round"/>
        <rect x="6" y="46" width="42" height="4" rx="2" fill="#1c7a3e"/>
      </svg>
      <span class="contact-text">0413862975</span>
    </div>

    <div class="contact-row email">
      <svg class="contact-icon" viewBox="0 0 54 54" aria-hidden="true">
        <rect x="2" y="2" width="50" height="50" rx="8" fill="#0b8ef2"/>
        <rect x="6" y="6" width="42" height="40" rx="6" fill="#46c8f8"/>
        <text x="27" y="34" text-anchor="middle" font-family="Arial, sans-serif" font-size="22" fill="#ffffff">@</text>
      </svg>
      <span class="contact-text">coreyh@pipeguardco.com.au</span>
    </div>

    <div class="motto">"Protecting Australia's Underground Utilities"</div>
    <div class="abn">A.B.N.52938470116</div>
  </div>
</div>
</body>
</html>
```